Lanterne architecture business cards

We are a new company based in New Zealand. We Specialize in High end Luxury Residential Architecture.

Every home is bespoke and is designed to each clients individual requirements and needs.

I like to design buildings that inspire people through light and form while offering a high level of comfort and usability.

Lines of sight, proportion and balance are fundamental to the spaces I create.
Updates

August 5th is current deadline - Today's date is the 13th of August.

Target Market(s)

New Zealanders who want a custom individual home design, typically 30-65 year old males and females

Industry/Entity Type

Architecture

Contact Information for Business Card

Director - Derek Tolson
Contact Number - 0279164073
Email - info@lanternearchitecture-example.co.nz
Webstie - www.lanternearchitecture-example.co.nz
Social Media - @lanternearchitecture

Font styles to use
Sans Serif

Requirements
Must have
• Logo (Both Sides)
Website
Email
Contact Number
Social Media

Nice to have
• Texture
Should not have
• More than 3 colours - typically I would've thought 2 would be good to match the logo.

```html
<!DOCTYPE html>
<html lang="en">
<head>
<meta charset="utf-8">
<title>Lanterne architecture business cards</title>
<link rel="stylesheet" href="https://fonts.googleapis.com/css2?family=Roboto:wght@300;400&display=swap">
<style>
  :root {
    --stage: #d6d6d8;
    --card-light: #e9ebf1;
    --card-dark-top: #4d4d4d;
    --card-dark-bottom: #303030;
    --ink: #3b3b3d;
    --ink-soft: #55565a;
    --tab: #3a3a3a;
    --icon-grey: #a9abb0;
    --logo-light: #f2f2f4;
  }
  * { margin: 0; padding: 0; box-sizing: border-box; }
  html, body {
    width: 1200px;
    height: 1200px;
    overflow: hidden;
    background: var(--stage);
    font-family: "Roboto", Arial, sans-serif;
  }
  .stage {
    position: relative;
    width: 1200px;
    height: 1200px;
  }
  .card {
    position: absolute;
    width: 640px;
    height: 390px;
    border-radius: 22px;
    overflow: hidden;
    box-shadow: 0 14px 30px rgba(0, 0, 0, 0.18);
  }

  /* Front: contact side */
  .card-front {
    left: 280px;
    top: 150px;
    background: var(--card-light);
    color: var(--ink);
  }
  .tab {
    position: absolute;
    width: 30px;
    background: var(--tab);
  }
  .tab-right { right: 0; top: 62px; height: 92px; }
  .tab-left { left: 0; top: 196px; height: 104px; }
  .holder-name {
    position: absolute;
    left: 92px;
    top: 62px;
    font-size: 42px;
    font-weight: 300;
    letter-spacing: 0.5px;
  }
  .holder-role {
    position: absolute;
    left: 96px;
    top: 114px;
    font-size: 19px;
    font-weight: 300;
    color: var(--ink-soft);
  }
  .social-row {
    position: absolute;
    left: 120px;
    top: 208px;
    display: flex;
    gap: 10px;
  }
  .social-square {
    width: 26px;
    height: 26px;
    border-radius: 5px;
    background: var(--icon-grey);
  }
  .contact-list {
    position: absolute;
    left: 96px;
    top: 244px;
    list-style: none;
    font-size: 18px;
    font-weight: 400;
    line-height: 24px;
    color: var(--ink);
  }
  .contact-item {
    display: flex;
    align-items: center;
    gap: 8px;
  }
  .contact-icon {
    width: 14px;
    height: 14px;
    flex: none;
  }
  .contact-icon.blank { visibility: hidden; }

  /* Back: logo side */
  .card-back {
    left: 280px;
    top: 640px;
    background: linear-gradient(135deg, var(--card-dark-top) 0%, var(--card-dark-bottom) 100%);
    color: var(--logo-light);
  }
  .brand {
    position: absolute;
    left: 0;
    right: 0;
    top: 88px;
    display: flex;
    flex-direction: column;
    align-items: center;
    font-weight: 300;
    color: var(--logo-light);
  }
  .brand-dot {
    width: 86px;
    height: 86px;
    border-radius: 50%;
    border: 10px solid var(--logo-light);
    margin-bottom: 44px;
  }
  .brand-name {
    font-size: 40px;
    letter-spacing: 16px;
    margin-right: -16px;
    line-height: 1;
  }
  .brand-sub {
    margin-top: 12px;
    font-size: 11px;
    letter-spacing: 16px;
    margin-right: -16px;
    line-height: 1;
  }
</style>
</head>
<body>
<main class="stage">
  <section class="card card-front" aria-label="Business card, contact side">
    <div class="tab tab-right"></div>
    <div class="tab tab-left"></div>
    <h1 class="holder-name">Derek Tolson</h1>
    <p class="holder-role">Director</p>
    <div class="social-row" aria-hidden="true">
      <span class="social-square"></span>
      <span class="social-square"></span>
      <span class="social-square"></span>
      <span class="social-square"></span>
    </div>
    <ul class="contact-list">
      <li class="contact-item">
        <svg class="contact-icon blank" viewBox="0 0 14 14"></svg>
        <span>@lanternearchitecture</span>
      </li>
      <li class="contact-item">
        <svg class="contact-icon" viewBox="0 0 14 14" aria-hidden="true">
          <path d="M3 1.5 L5 1.5 L6 4.5 L4.6 5.6 Q5.6 8 8.4 9.4 L9.5 8 L12.5 9 L12.5 11 Q12 12.5 10.5 12.5 Q5 12 1.5 4 Q1.5 2 3 1.5 Z" fill="var(--ink)"/>
        </svg>
        <span>0279164073</span>
      </li>
      <li class="contact-item">
        <svg class="contact-icon" viewBox="0 0 14 14" aria-hidden="true">
          <rect x="1.5" y="3" width="11" height="8" fill="none" stroke="var(--ink)" stroke-width="1.4"/>
          <path d="M1.5 3 L7 7.5 L12.5 3" fill="none" stroke="var(--ink)" stroke-width="1.4"/>
        </svg>
        <span>info@lanternearchitecture-example.co.nz</span>
      </li>
      <li class="contact-item">
        <svg class="contact-icon" viewBox="0 0 14 14" aria-hidden="true">
          <circle cx="7" cy="7" r="5.5" fill="none" stroke="var(--ink)" stroke-width="1.3"/>
          <ellipse cx="7" cy="7" rx="2.4" ry="5.5" fill="none" stroke="var(--ink)" stroke-width="1.1"/>
          <line x1="1.5" y1="7" x2="12.5" y2="7" stroke="var(--ink)" stroke-width="1.1"/>
        </svg>
        <span>www.lanternearchitecture-example.co.nz</span>
      </li>
    </ul>
  </section>

  <section class="card card-back" aria-label="Business card, logo side">
    <div class="brand">
      <span class="brand-dot" aria-hidden="true"></span>
      <span class="brand-name">LANTERNE</span>
      <span class="brand-sub">ARCHITECTURE</span>
    </div>
  </section>
</main>
</body>
</html>
```